Web Design Project

My website was fine - years ago. But it's way, way overdue for an overhaul. When I started my business almost 20 years ago, I wanted to be edgy. And my website was just that. Color, style, voice. Edgy. Today, my clients are corporations. I'm older, more experienced - but still a little edgy. It's controlled edge. What I want now is sophisticated. Savvy. Corporate but cool. Grown up.

My clients are primarily - but not exclusively - in healthcare. But I don't want a healthcare site. I provide the following services:
1. Writing - white papers, brochures, web pages, speechwriting, etc.
2. Marketing strategy
3. Public relations services
4. Thought leader development
5. Training
I couldn't upload all the icons but I can send them. They correspond with the pages as follows and should be used in the design:

1. Writing- nib.png
2. Marketing strategy-compass.png
3. Public relations services-microphone.png
4. Thought leader development-lightbulb.png
5. Training: cogs-training.png or key.png

I will have a blog, and a portfolio of some kind.

I don't want something that looks like a template.
Updates

Reason: Just made this a committed payment. I apologize for not doing so from the start. Nobody should work for free.

Reason: Several folks have asked to resubmit, and it has taken me a while to provide feedback.

Dear Designers,

I am so sorry to have been so slow to select. I've had professional and personal issues to deal with. I am actively trying to select a design, however, and will do so in the next two days. Thanks so much for your patience and hard work.

Rhoda

Thanks so much to everyone who has submitted a design. I had great luck crowdsourcing my logo, but I'm starting to realize that website design is a totally different animal. All of your designs are great, but they all look exactly like templates. And maybe that's the way it's supposed to be, the way it should be. I don't want to use stock photography. It needs to be more personalized than that. I'm open to illustration or even using my own photo on the site, but stock photography won't work for me. If anyone wants to submit something else - and I understand if you don't - please feel free. 

Target Market(s)

C-suite executives; corporations, larger businesses who need marketing writing

Industry/Entity Type

Healthcare

Requirements
Must have
• Logo (somewhere)
Icons
Nice to have
• Level-specific page design (e.g, Home = Level 1, Tabs = Level 2, etc). I'd like it to have a certain order.

```html
<!DOCTYPE html>
<html lang="en">
<head>
<meta charset="utf-8">
<title>The Apex — Communication Services</title>
<link href="https://fonts.googleapis.com/css2?family=Arimo:wght@400;700&display=swap" rel="stylesheet">
<style>
  :root {
    --bg-deep: #4a2f6e;
    --bg-mid: #7c4d9e;
    --bg-glow: #a874c4;
    --purple: #8a3fb0;
    --purple-dark: #5b2a7e;
    --band: #c09cdc;
    --orange: #f39a1e;
    --ink: #3a3a3a;
    --muted: #777777;
    --white: #ffffff;
    --footer: #f2e8e8;
  }
  * { margin: 0; padding: 0; box-sizing: border-box; }
  html, body { width: 960px; height: 1200px; overflow: hidden; }
  body {
    position: relative;
    font-family: "Arimo", Arial, sans-serif;
    background: radial-gradient(ellipse at 15% 45%, var(--bg-glow) 0%, var(--bg-mid) 35%, var(--bg-deep) 90%);
    color: var(--ink);
  }
  .abs { position: absolute; }

  .utility-icons { left: 746px; top: 4px; display: flex; gap: 22px; }
  .utility-icons svg { width: 16px; height: 12px; fill: var(--white); }

  .site-header { left: 104px; top: 24px; width: 768px; height: 66px; background: #f8f7fb; }
  .brand-mark { left: 14px; top: 9px; width: 48px; height: 48px; background: var(--purple-dark); border-radius: 50%; }
  .brand-name { left: 76px; top: 13px; font-size: 26px; font-weight: 400; color: var(--purple-dark); letter-spacing: 1px; }
  .brand-tagline { left: 77px; top: 44px; font-size: 9px; color: var(--muted); letter-spacing: .4px; }
  .main-nav { right: 12px; top: 37px; display: flex; gap: 24px; font-size: 13.5px; color: var(--purple); }

  .hero { left: 104px; top: 92px; width: 770px; height: 286px;
    background: linear-gradient(180deg, #8ea6c8 0%, #a9b7c8 18%, #9a9a9a 30%, #888 70%, #6e6e6e 100%); }
  .hero-caption { left: 47px; top: 48px; width: 249px; height: 116px; background: rgba(60,60,66,.72); color: var(--white); padding: 16px 16px 0 17px; }
  .hero-caption h2 { font-weight: 400; font-size: 13px; line-height: 17px; letter-spacing: .6px; margin-left: 3px; }
  .hero-caption p { font-size: 9.6px; line-height: 13.4px; margin-top: 8px; }

  .content { left: 104px; top: 382px; width: 770px; height: 672px; background: var(--white); }
  .welcome-title { left: 38px; top: 20px; font-size: 27px; font-weight: 400; letter-spacing: 1px; color: #333; }
  .welcome-text { left: 34px; top: 62px; width: 714px; font-size: 9.9px; line-height: 13.5px; color: #444; }

  .band { height: 64px; background: var(--band); }
  .band-left { left: 0; width: 320px; }
  .band-right { right: 0; width: 320px; }
  .band-title { font-size: 17px; line-height: 23px; color: var(--purple-dark); letter-spacing: .2px; }
  .badge { width: 92px; height: 92px; border-radius: 50%; background: var(--band); display: flex; align-items: center; justify-content: center; }
  .badge-icon { width: 70px; height: 70px; border-radius: 50%; border: 2px solid var(--orange);
    background: radial-gradient(circle at 40% 35%, #9a3fb8 0%, #6a1f8a 70%); }
  .service-text { width: 312px; font-size: 9.9px; line-height: 13.6px; text-align: center; color: #444; }

  .site-footer { left: 104px; top: 1058px; width: 770px; height: 118px; background: var(--footer); }
  .footer-nav { left: 0; top: 8px; width: 100%; text-align: center; font-size: 13.6px; letter-spacing: 1.3px; color: #333; word-spacing: 6px; }
  .social { left: 356px; top: 64px; display: flex; gap: 12px; }
  .social span { width: 24px; height: 24px; border-radius: 50%; background: var(--white); border: 1px solid #ddd; }
  .legal { left: 0; top: 98px; width: 100%; text-align: center; font-size: 8.6px; color: #444; }
  .copyright { left: 0; top: 1182px; width: 960px; text-align: center; font-size: 8.8px; color: var(--white); }
</style>
</head>
<body>

<div class="abs utility-icons">
  <svg viewBox="0 0 16 12" aria-label="Home"><path d="M8 0 16 6h-2v6h-4V8H6v4H2V6H0z"/></svg>
  <svg viewBox="0 0 16 12" aria-label="Phone"><path d="M1 4c0-2 3-3 7-3s7 1 7 3v1h-4V3.5H5V5H1zM4 6h8l2 5H2z"/></svg>
  <svg viewBox="0 0 16 12" aria-label="Email"><path d="M1 1h14v10H1zM2 2.5v.5l6 4 6-4v-.5z"/></svg>
</div>

<header class="abs site-header">
  <div class="abs brand-mark"></div>
  <div class="abs brand-name">THE APEX</div>
  <div class="abs brand-tagline">CLEAR WORDS FOR COMPLEX WORK</div>
  <nav class="abs main-nav">
    <span>Home</span><span>About</span><span>Services</span><span>Portfolio</span><span>Contact</span><span>Blog</span>
  </nav>
</header>

<section class="abs hero" role="img" aria-label="Photo of two businessmen in suits walking up wide stone steps under a cloudy sky">
  <div class="abs hero-caption">
    <h2>Discover the markets<br>you’ve never approached....</h2>
    <p>Lorem ipsum dolor sit amet, consectetuer libero. Suspendisse bibendum. Cras id urna. Morbi tincidunt, orci ac</p>
  </div>
</section>

<main class="abs content">
  <h1 class="abs welcome-title">Welcome</h1>
  <p class="abs welcome-text">Lorem ipsum dolor sit amet, consectetuer adipiscing elit. Donec libero. Suspendisse bibendum. Cras id urna. Morbi tincidunt, orci ac convallis aliquam, lectus turpis varius lorem, eu posuere nunc justo tempus leo. Donec mattis, purus nec placerat bibendum, dui pede condimentum odio, ac blandit ante orci ut diam. Cras fringilla magna. Phasellus suscipit, leo a pharetra condimentum, lorem tellus eleifend magna, eget fringilla velit magna id neque. Curabitur vel urna. In tristique orci porttitor ipsum. Lorem ipsum dolor sit amet, consectetuer adipiscing elit. Donec libero. Suspendisse bibendum. Cras id urna. Morbi tincidunt, orci ac convallis aliquam, lectus turpis varius lorem, eu posuere nunc justo tempus leo.Aenean consequat porttitor adipiscing. Nam pellentesque justo ut tortor congue lobortis. Donec venenatis sagittis fringilla. Etiam nec libero magna, et dictum velit. Proin mauris mauris, mattis eu elementum eget, commodo in nulla. Mauris posuere venenatis pretium. Maecenas a dui sed lorem aliquam dictum. Nunc urna leo, imperdiet eu bibendum ac, pretium ac massa. Cum sociis natoque penatibus et magnis dis parturient montes, nascetur ridiculus mus. Nulla facilisi Quisque condimentum luctus ullamcorper.</p>

  <div class="abs band band-left" style="top:229px;"></div>
  <div class="abs band-title" style="left:23px;top:249px;">WRITTING</div>
  <div class="abs badge" style="left:270px;top:218px;"><div class="badge-icon" role="img" aria-label="Writing service icon"></div></div>
  <p class="abs service-text" style="left:440px;top:226px;">Lorem ipsum dolor sit amet, consectetuer adipiscing elit. Donec libero. Suspendisse bibendum. Cras id urna. Morbi tincidunt, orci ac onvallis aliquam, lectus turpis varius lorem, eu posuere nunc justo tempuleo. Donec mattis, purus nec placerat bibendum, dui pede</p>

  <div class="abs band band-right" style="top:312px;"></div>
  <div class="abs band-title" style="left:514px;top:332px;">MARKETING STRATERGY</div>
  <div class="abs badge" style="left:408px;top:294px;"><div class="badge-icon" role="img" aria-label="Marketing strategy compass icon"></div></div>
  <p class="abs service-text" style="left:26px;top:324px;">Lorem ipsum dolor sit amet, consectetuer adipiscing elit. Donec libero. Suspendisse bibendum. Cras id urna. Morbi tincidunt, orci ac onvallis aliquam, lectus turpis varius lorem, eu posuere nunc justo tempuleo. Donec mattis, purus nec placerat bibendum, dui pede</p>

  <div class="abs band band-left" style="top:399px;"></div>
  <div class="abs band-title" style="left:27px;top:408px;">PUBLIC RELATIONS<br>SERVICES</div>
  <div class="abs badge" style="left:270px;top:388px;"><div class="badge-icon" role="img" aria-label="Public relations service icon"></div></div>
  <p class="abs service-text" style="left:438px;top:404px;">Lorem ipsum dolor sit amet, consectetuer adipiscing elit. Donec libero. Suspendisse bibendum. Cras id urna. Morbi tincidunt, orci ac onvallis aliquam, lectus turpis varius lorem, eu posuere nunc justo tempuleo. Donec mattis, purus nec placerat bibendum, dui pede</p>

  <div class="abs band band-right" style="top:494px;"></div>
  <div class="abs band-title" style="left:523px;top:503px;">THOUGHT LEADER<br>DEVELOPMENT</div>
  <div class="abs badge" style="left:408px;top:476px;"><div class="badge-icon" role="img" aria-label="Thought leader development lightbulb icon"></div></div>
  <p class="abs service-text" style="left:22px;top:496px;">Lorem ipsum dolor sit amet, consectetuer adipiscing elit. Donec libero. Suspendisse bibendum. Cras id urna. Morbi tincidunt, orci ac onvallis aliquam, lectus turpis varius lorem, eu posuere nunc justo tempuleo. Donec mattis, purus nec placerat bibendum, dui pede</p>

  <div class="abs band band-left" style="top:580px;"></div>
  <div class="abs band-title" style="left:27px;top:600px;">TRAINNING</div>
  <div class="abs badge" style="left:272px;top:568px;"><div class="badge-icon" role="img" aria-label="Training key icon"></div></div>
  <p class="abs service-text" style="left:434px;top:592px;">Lorem ipsum dolor sit amet, consectetuer adipiscing elit. Donec libero. Suspendisse bibendum. Cras id urna. Morbi tincidunt, orci ac onvallis aliquam, lectus turpis varius lorem, eu posuere nunc justo tempuleo. Donec mattis, purus nec placerat bibendum, dui pede</p>
</main>

<footer class="abs site-footer">
  <nav class="abs footer-nav">Home . About . Services . Portfolio . Contact . Blog</nav>
  <div class="abs social" aria-label="Social links"><span></span><span></span></div>
  <div class="abs legal">Privacy Policy &nbsp;|&nbsp; Terms and Conditions &nbsp;|&nbsp; Cookies</div>
</footer>
<div class="abs copyright">Copyright © 2013 The Apex. All rights reserved</div>

</body>
</html>
```